French for French

Cover for the book "The Plume Vagabonde" ("How to write in French"). The book seeks to teach English to English: words, grammar, syntax. The lessons are pleasant, the style is very classical.

Target Market(s)

Middle class interested in improving her language.

Industry/Entity Type

Publishing Company

Colors

Designer to choose colors to be used in the design.

Requirements
Must have
• Author: "Marcel Tournevin" Title: "The Roving Quill" Publisher: "Corvane Editions" Size: 14 x 20,5 cm

```html
<!DOCTYPE html>
<html lang="fr">
<head>
<meta charset="utf-8">
<title>La Plume Vagabonde — Marcel Tournevin</title>
<link rel="stylesheet" href="https://fonts.googleapis.com/css2?family=Cinzel:wght@400&family=Crimson+Text:wght@400&family=Lato:wght@400&display=swap">
<style>
  :root {
    --paper: #ffffff;
    --ink: #1a1a1a;
    --navy: #2e2a5c;
    --navy-soft: #4b4aa0;
    --rose: #ea2360;
    --rose-soft: #f36a8e;
    --title: #ffffff;
    --publisher: #e8384a;
    --scene-warm: #f3c98a;
    --scene-coral: #e8583e;
  }
  * { margin: 0; padding: 0; box-sizing: border-box; }
  html, body { width: 819px; height: 1200px; overflow: hidden; background: var(--paper); }
  .cover { position: relative; width: 819px; height: 1200px; background: var(--paper); overflow: hidden; }
  .author {
    position: absolute; top: 48px; left: 0; width: 100%;
    text-align: center;
    font-family: "Cinzel", serif; font-size: 40px; letter-spacing: 0.32em;
    color: var(--ink); text-transform: uppercase;
  }
  .paint-bands { position: absolute; inset: 0; }
  .title {
    position: absolute; top: 322px; left: 0; width: 100%;
    text-align: center;
    font-family: "Crimson Text", serif; font-size: 100px; line-height: 112px;
    color: var(--title);
    text-shadow: 3px 4px 6px rgba(0,0,0,0.35);
  }
  .scene {
    position: absolute; left: 160px; top: 585px; width: 510px; height: 430px;
    border-radius: 40px;
    background: radial-gradient(ellipse at 50% 30%, var(--scene-warm) 0%, rgba(243,201,138,0.45) 40%, rgba(232,88,62,0.18) 70%, rgba(255,255,255,0) 100%);
  }
  .publisher {
    position: absolute; top: 1098px; left: 0; width: 100%;
    text-align: center;
    font-family: "Lato", sans-serif; font-size: 36px;
    color: var(--publisher);
  }
</style>
</head>
<body>
  <main class="cover">
    <p class="author">Marcel Tournevin</p>

    <svg class="paint-bands" width="819" height="1200" viewBox="0 0 819 1200" aria-hidden="true">
      <polygon points="40,480 70,340 700,128 760,150 770,270 95,515" fill="var(--navy-soft)" opacity="0.55"/>
      <polygon points="50,470 80,350 705,140 755,160 765,262 100,500" fill="var(--navy)"/>
      <polygon points="55,720 95,565 819,285 819,470 120,765" fill="var(--rose-soft)" opacity="0.5"/>
      <polygon points="65,705 105,575 819,300 819,450 125,745" fill="var(--rose)"/>
    </svg>

    <h1 class="title">La Plume<br>Vagabonde</h1>

    <div class="scene" role="img" aria-label="Illustration : deux femmes assises à une terrasse de café sous un parasol jaune, avec une lanterne murale"></div>

    <p class="publisher">Editions Corvane</p>
  </main>
</body>
</html>
```